Design some Business Cards for QR-TOP

I have a logo that I am pleased with, but it needs to be sharpened up. I would like to use the refined logo for business cards and packaging. I have a new product that I am going to do market research on and decide if the market will allow me to pursue it further. If things go right I will build a website. I would like to keep the business cards, packaging, and website very similar.

```html
<!DOCTYPE html>
<html lang="en">
<head>
<meta charset="utf-8">
<title>QR-TOP Business Cards</title>
<link href="https://fonts.googleapis.com/css2?family=Open+Sans:wght@400;600;800&family=Old+Standard+TT:wght@400&display=swap" rel="stylesheet">
<style>
  :root {
    --page-bg: #e9e6e1;
    --card-bg: #33363f;
    --card-band: #454852;
    --card-edge: #b8121b;
    --accent-red: #d4222b;
    --text-light: #ffffff;
    --text-muted: #b9bcc4;
  }
  * { margin: 0; padding: 0; box-sizing: border-box; }
  html, body { width: 1200px; height: 900px; overflow: hidden; }
  body {
    background: var(--page-bg);
    font-family: "Open Sans", Arial, sans-serif;
    display: flex;
    align-items: center;
    justify-content: center;
    gap: 56px;
  }
  .card {
    position: relative;
    width: 520px;
    height: 300px;
    background: var(--card-bg);
    border: 8px solid var(--card-edge);
    border-radius: 4px;
    overflow: hidden;
    box-shadow: 0 10px 24px rgba(0,0,0,0.18);
  }

  /* Front */
  .card-front {
    display: flex;
    flex-direction: column;
    align-items: center;
    justify-content: center;
  }
  .brand-name {
    font-family: "Open Sans", Arial, sans-serif;
    font-weight: 800;
    color: var(--text-light);
    letter-spacing: 1px;
  }
  .card-front .brand-name { font-size: 72px; line-height: 1; }
  .brand-subname {
    font-family: "Old Standard TT", Georgia, serif;
    color: var(--accent-red);
    font-size: 30px;
    letter-spacing: 3px;
    margin-top: 10px;
  }
  .front-web {
    color: var(--text-light);
    font-size: 20px;
    letter-spacing: 5px;
    margin-top: 14px;
  }

  /* Back */
  .back-band {
    position: absolute;
    inset: 0;
    width: 100%;
    height: 100%;
  }
  .back-brand {
    position: absolute;
    left: 36px;
    top: 52px;
  }
  .back-brand .brand-name { font-size: 44px; line-height: 1; }
  .slogan {
    color: var(--text-muted);
    font-size: 12px;
    margin-top: 8px;
    letter-spacing: 0.5px;
  }
  .back-details {
    position: absolute;
    left: 270px;
    top: 120px;
  }
  .back-details .brand-subname { font-size: 24px; margin: 0 0 10px 0; }
  .contact-list { list-style: none; }
  .contact-item {
    display: flex;
    align-items: center;
    gap: 10px;
    color: var(--text-light);
    font-size: 12px;
    margin-bottom: 7px;
  }
  .contact-icon { width: 16px; height: 16px; flex: none; }
</style>
</head>
<body>

  <section class="card card-front" aria-label="Business card front">
    <div class="brand-name">QR-TOP</div>
    <div class="brand-subname">QR-TOP</div>
    <div class="front-web">www.qrtop-site.com</div>
  </section>

  <section class="card card-back" aria-label="Business card back">
    <svg class="back-band" viewBox="0 0 504 284" preserveAspectRatio="none" aria-hidden="true">
      <polygon points="0,40 60,40 330,40 380,110 250,110 220,150 0,150" fill="var(--card-band)"/>
    </svg>

    <div class="back-brand">
      <div class="brand-name">QR-TOP</div>
      <div class="slogan">Slogan tags here...</div>
    </div>

    <div class="back-details">
      <div class="brand-subname">QR-TOP</div>
      <ul class="contact-list">
        <li class="contact-item">
          <svg class="contact-icon" viewBox="0 0 16 16" aria-hidden="true">
            <rect x="1.5" y="3.5" width="13" height="9" fill="none" stroke="var(--accent-red)" stroke-width="1.4"/>
            <polyline points="1.5,3.5 8,9 14.5,3.5" fill="none" stroke="var(--accent-red)" stroke-width="1.4"/>
          </svg>
          hello@qrtop-mail.com
        </li>
        <li class="contact-item">
          <svg class="contact-icon" viewBox="0 0 16 16" aria-hidden="true">
            <circle cx="8" cy="8" r="8" fill="var(--text-light)"/>
            <polygon points="8,3.5 12.5,7.5 11,7.5 11,12 5,12 5,7.5 3.5,7.5" fill="var(--card-bg)"/>
          </svg>
          27 Harbor Lane, Easton
        </li>
        <li class="contact-item">
          <svg class="contact-icon" viewBox="0 0 16 16" aria-hidden="true">
            <circle cx="8" cy="8" r="8" fill="var(--text-light)"/>
            <path d="M5.5 4 L7 4 L7.6 6.2 L6.6 7 Q7.3 8.6 9 9.4 L9.8 8.4 L12 9 L12 10.5 Q11.5 12 10 12 Q5 11.3 4 6 Q4 4.5 5.5 4 Z" fill="var(--card-bg)"/>
          </svg>
          555014287
        </li>
        <li class="contact-item">
          <svg class="contact-icon" viewBox="0 0 16 16" aria-hidden="true">
            <circle cx="8" cy="8" r="6.5" fill="none" stroke="var(--accent-red)" stroke-width="1.4"/>
            <ellipse cx="8" cy="8" rx="2.8" ry="6.5" fill="none" stroke="var(--accent-red)" stroke-width="1.1"/>
            <line x1="1.5" y1="8" x2="14.5" y2="8" stroke="var(--accent-red)" stroke-width="1.1"/>
          </svg>
          www.qrtop-site.com
        </li>
      </ul>
    </div>
  </section>

</body>
</html>
```